7 Reeds Distillery - Bottle Label Design

We are a small craft distillery whose branding needs to incorporate our location on a lake (Lac Vorbelle, Quebec, Canada). A unique aspect of the lake is that people drive floating docks on the lake powered by a small outboard motor (see photos). Back in the 1970’s when Lac Vorbelle was a sparsely populated and difficult-to-access lake in the Gatineau Hills north of Ottawa, the concept of motorized docks was conjured on a lazy afternoon and this single stroke of genius has inadvertently spawned the most exceptional and eccentric lake based community. Throughout the summer, somewhere around four o’clock on any given Friday and Saturday it starts to happen. Docks set sail from their customary landing places - family, friends, snacks and loaded drink coolers in-tow and, as if magnetically drawn, head toward Heron Shoal. Without fail they will come upon a gathering of similar minded floating docks within the vicinity - be guided in with help to moor alongside and within seconds be seamlessly immersed in the festivities. Seldom any longer are these events planned, they have become elemental, a thing organically derived from within the community. This on-going weekly event is the genesis of the strong bond that brings us Seven Reeds Distilling.
Each of the 4 distillery owners have one of these docks so hence the name. We are open to either "7 Reeds" or spelled out as "Seven Reeds" as may be visually appropriate. We are also open to "Distillery" or "Distilling". More detail on the docks themselves, they are 14x16 feet powered by a small outboard motor as shown in the photos. This dock aspect may be difficult to incorporate into the branding but the lake outline is included as an image applicable to include for that local reference aspect. We will be creating very high quality small batch liquors such as vodka, rum, gin and whiskey. Each batch will be triple distilled and perhaps 20 bottles in quantity so very exclusive. We are aiming at a premium feel for the branding. Attached are some bottle label designs that evoke the type of feel we are going for and a photo of the style of blank bottle to design for which is a 750ml Nordic pattern bottle.
In general we are going for more contemporary than traditional, more bold than delicate. If a single label the size desired would be 4 inches wide and 4 inches tall. If a double/split label as in two of the photos the top label would be 3 inches wide and 3 inches tall and the bottom label would be max 4 inches wide and 1.5 inches tall. We are open to the upper label being a "transparent" label to create a printed on bottle effect, perhaps of the brand logo. We are only interested in front label so do not require a back, neck or closure label. The label will require the ability to name the batch style name (example "Tuberov") and then the amplifying information for the type of alcohol (Russian Potato Vodka) in a smaller font. Another example ("Bell Cap" and "London Dry Gin"). Information for bottle size (750ml) and alcohol % (40%) are also to be included. Governmental safety warnings are not required. We are open to use of any colours in the label. The basic label design would be re-used for different types of batches where we would change the style and alcohol name.

Target Market(s)

Up scale premium spirits buyers

Font styles to use
Serif
Sans Serif

Requirements
Must have
• A visual reference to the docks or the lake per the images attached.
Nice to have
• Ideally we can re-use the label design for a different type of Alcohol by changing the alcohol name and style information and maybe the colour of a major element in the label.

```html
<!DOCTYPE html>
<html lang="en">
<head>
<meta charset="utf-8">
<title>7 Reeds Distillery – Front Labels</title>
<link rel="stylesheet" href="https://fonts.googleapis.com/css2?family=Barlow+Condensed:wght@400;500;600&display=swap">
<style>
  :root {
    --canvas: #f4f4f4;
    --ink: #2f2f2f;
    --ink-soft: #4a4a4a;
    --teal-light: #c6e6e5;
    --teal-mid: #86c4c3;
    --teal-deep: #63a8a7;
    --gold: #e7b41f;
    --gold-text: #e3b11e;
    --photo-light: #b8b8b8;
    --photo-dark: #555555;
    --rule: #2f2f2f;
  }
  * { box-sizing: border-box; margin: 0; padding: 0; }
  html, body { width: 1200px; height: 960px; overflow: hidden; }
  body {
    background: var(--canvas);
    font-family: "Barlow Condensed", "Arial Narrow", sans-serif;
    color: var(--ink);
    display: flex;
    justify-content: center;
    align-items: center;
    gap: 150px;
  }
  .label {
    width: 330px;
    display: flex;
    flex-direction: column;
    align-items: center;
  }

  /* Top "printed on glass" area */
  .style-name {
    font-weight: 600;
    font-size: 74px;
    line-height: 1;
    letter-spacing: 0.12em;
    margin-right: -0.12em;
    text-transform: uppercase;
  }
  .spirit-type {
    display: flex;
    align-items: center;
    gap: 10px;
    font-weight: 500;
    font-size: 32px;
    line-height: 1;
    color: var(--ink-soft);
    margin-top: 8px;
  }
  .spirit-type::before, .spirit-type::after {
    content: "";
    width: 28px;
    height: 1.5px;
    background: var(--rule);
  }
  .spirit {
    font-weight: 600;
    line-height: 0.86;
    letter-spacing: -0.02em;
  }

  /* Vodka label */
  .label--vodka .style-name,
  .label--vodka .spirit {
    background: linear-gradient(90deg, var(--teal-light), var(--teal-deep));
    -webkit-background-clip: text;
    background-clip: text;
    color: transparent;
  }
  .label--vodka .spirit { font-size: 132px; margin-top: 2px; }
  .label--vodka .band {
    width: 100%;
    height: 188px;
    margin-top: 8px;
    background: linear-gradient(90deg, var(--teal-light), var(--teal-mid) 55%, var(--teal-deep));
    display: flex;
    flex-direction: column;
    justify-content: flex-end;
  }
  .label--vodka .brand-name {
    text-align: center;
    margin-bottom: 12px;
  }
  .info-row {
    display: flex;
    border-top: 1.5px solid var(--rule);
    height: 32px;
    font-size: 15px;
    color: var(--ink-soft);
  }
  .info-row span {
    flex: 1;
    display: flex;
    align-items: center;
    padding: 0 30px;
  }
  .info-row span + span {
    border-left: 1.5px solid var(--rule);
    justify-content: flex-end;
  }

  .brand-name {
    font-weight: 600;
    font-size: 21px;
    letter-spacing: 0.22em;
    color: var(--ink);
    text-transform: uppercase;
    white-space: nowrap;
  }

  /* Gin label */
  .label--gin .style-name,
  .label--gin .spirit { color: var(--gold-text); }
  .label--gin .spirit { font-size: 124px; margin-top: 8px; }
  .label--gin .spirit-type { color: var(--ink); }
  .dock-photo {
    width: 100%;
    height: 112px;
    margin-top: 6px;
    background: linear-gradient(180deg, var(--photo-dark) 0%, var(--photo-light) 45%, #8c8c8c 70%, var(--photo-dark) 100%);
  }
  .label--gin .band {
    width: 100%;
    height: 76px;
    background: var(--gold);
    display: flex;
  }
  .label--gin .brand-cell {
    flex: 1;
    display: flex;
    align-items: center;
    justify-content: center;
    gap: 10px;
  }
  .brand-mark {
    width: 14px;
    height: 14px;
    background: var(--ink);
  }
  .label--gin .brand-name { font-size: 19px; letter-spacing: 0.18em; }
  .info-stack {
    width: 62px;
    border-left: 1.5px solid var(--rule);
    display: flex;
    flex-direction: column;
    font-size: 13px;
    line-height: 1.05;
    text-align: center;
    color: var(--ink);
  }
  .info-stack span {
    flex: 1;
    display: flex;
    align-items: center;
    justify-content: center;
  }
  .info-stack span + span { border-top: 1.5px solid var(--rule); flex: 0.7; }
</style>
</head>
<body>

  <section class="label label--vodka">
    <h1 class="style-name">Tuberov</h1>
    <p class="spirit-type">Russian Potato</p>
    <p class="spirit">Vodka</p>
    <div class="band">
      <p class="brand-name">7 Reeds Distillery</p>
      <div class="info-row">
        <span>Alcohol 40%</span>
        <span>750ml</span>
      </div>
    </div>
  </section>

  <section class="label label--gin">
    <h1 class="style-name">Bell Cap</h1>
    <p class="spirit-type">London Dry</p>
    <p class="spirit">Gin</p>
    <div class="dock-photo" role="img" aria-label="Black and white photo of floating docks gathered on the lake shore"></div>
    <div class="band">
      <div class="brand-cell">
        <span class="brand-mark"></span>
        <p class="brand-name">7 Reeds Distillery</p>
      </div>
      <div class="info-stack">
        <span>Alcohol<br>40%</span>
        <span>750ml</span>
      </div>
    </div>
  </section>

</body>
</html>
```